Tarvel Ridge LLC

Need Professional Business cards for New Investment Fund

Target Market(s)

High Quality investors

Industry/Entity Type

Financial

Contact Information for Business Card

Phone Number +1 555 284 6193
Name Pavel Orlinsky
Title Fund Manager
email po@FundTarvel.example
Website www.FundTarvel.example

Colors

Designer to choose colors to be used in the design.

Requirements
Must have
• Must have our Logo and all of the above. Must be made so lettering and loge can be raised

```html
<!DOCTYPE html>
<html lang="en">
<head>
<meta charset="utf-8">
<title>Tarvel Ridge LLC – Business Card</title>
<link rel="stylesheet" href="https://fonts.googleapis.com/css2?family=Roboto:wght@400;500;700&display=swap">
<style>
  :root {
    --page-bg: #e6e6e6;
    --card-white: #ffffff;
    --forest: #434f43;
    --leaf: #5bbb46;
    --ink-grey: #6b6b6b;
    --paper-white: #ffffff;
  }
  * { box-sizing: border-box; margin: 0; padding: 0; }
  html, body {
    width: 1125px; height: 1200px; overflow: hidden;
    background: var(--page-bg);
    font-family: "Roboto", Arial, sans-serif;
  }
  .canvas { position: relative; width: 1125px; height: 1200px; }
  .card {
    position: absolute; left: 92px; width: 940px; height: 537px;
    border-radius: 30px; overflow: hidden;
  }
  .card--front { top: 38px; background: var(--card-white); }
  .card--back { top: 625px; background: var(--forest); }
  .card__band {
    position: absolute; left: 0; right: 0; bottom: 0; height: 20px;
    background: var(--leaf);
  }
  .brand {
    position: absolute; display: flex; align-items: center; gap: 10px;
    font-weight: 700; white-space: nowrap;
  }
  .brand__mark { display: block; background: var(--leaf); }
  .card--front .brand {
    left: 268px; top: 250px; font-size: 26px; color: var(--forest);
  }
  .card--front .brand__mark { width: 18px; height: 18px; }
  .card--back .brand {
    left: 50%; top: 50%; transform: translate(-50%, -50%);
    font-size: 48px; color: var(--paper-white); gap: 16px;
  }
  .card--back .brand__mark { width: 32px; height: 32px; }
  .divider {
    position: absolute; left: 469px; top: 177px; width: 2px; height: 180px;
    background: var(--leaf);
  }
  .contact { position: absolute; left: 512px; top: 172px; }
  .contact__name {
    font-weight: 700; font-size: 30px; color: var(--forest); line-height: 1.2;
  }
  .contact__title {
    font-weight: 400; font-size: 22px; color: var(--leaf); margin-top: 4px;
  }
  .contact__list { list-style: none; margin-top: 26px; }
  .contact__item {
    display: flex; align-items: center; gap: 12px;
    font-size: 21px; color: var(--ink-grey); height: 37px;
  }
  .contact__icon { width: 16px; height: 16px; flex: none; }
</style>
</head>
<body>
<div class="canvas">

  <section class="card card--front">
    <div class="brand"><span class="brand__mark"></span>Tarvel Ridge</div>
    <div class="divider"></div>
    <div class="contact">
      <h1 class="contact__name">Pavel Orlinsky</h1>
      <p class="contact__title">Fund Manager</p>
      <ul class="contact__list">
        <li class="contact__item">
          <svg class="contact__icon" viewBox="0 0 16 16" aria-hidden="true">
            <rect x="4" y="1" width="8" height="14" rx="1.5" fill="none" stroke="#434f43" stroke-width="1.6"/>
            <rect x="7" y="12" width="2" height="1.4" fill="#434f43"/>
          </svg>
          +1 555 284 6193
        </li>
        <li class="contact__item">
          <svg class="contact__icon" viewBox="0 0 16 16" aria-hidden="true">
            <rect x="1" y="3" width="14" height="10" rx="1" fill="#434f43"/>
            <path d="M2.5 4.5 L8 9 L13.5 4.5" fill="none" stroke="#fff" stroke-width="1.4"/>
          </svg>
          po@FundTarvel.example
        </li>
        <li class="contact__item">
          <svg class="contact__icon" viewBox="0 0 16 16" aria-hidden="true">
            <circle cx="8" cy="8" r="7" fill="#434f43"/>
            <path d="M4 5 Q6 4 7 6 Q6 8 8 9 Q9 11 7 13 M10 3 Q12 5 11 7 Q13 8 13 10" fill="none" stroke="#fff" stroke-width="1.2"/>
          </svg>
          www.FundTarvel.example
        </li>
      </ul>
    </div>
    <div class="card__band"></div>
  </section>

  <section class="card card--back">
    <div class="brand"><span class="brand__mark"></span>Tarvel Ridge</div>
    <div class="card__band"></div>
  </section>

</div>
</body>
</html>
```